Weihnachtsbanner Vortan Tidal Seat Sale & 50% on selected items
Zielgruppe
Wir vertreiben online Designklassiker im Bereich Möbel, Leuchten & Accessoires.
Zu Weihnachten möchten wir 24 Tidal Seat´s zu 799,-Euro verkaufen, statt 1998,-Euro.
Only 24 pieces & only while stock lasts!
Bannergrößen: 1130x542
Aufgabenstellung
Wir benötigen einen Banner indem wir 24 Tidal Seat´s zu 799,-Euro anbieten, statt 1998,-Euro.
Christmas Special - Only 24 pieces & only while stock lasts!
Der Banner sollte dezent sein und weihnachtlich dekoriert sein.
Danach benötigen wir noch einen zweiten Banner, welcher 50% auf ausgelesene Produkte hinweisen tut. Siehe Beispiel (Bild 2)
50% OFF on selected items!

```html
<!DOCTYPE html>
<html lang="en">
<head>
<meta charset="utf-8">
<title>Christmas Special – Tidal Seat</title>
<link rel="stylesheet" href="https://fonts.googleapis.com/css2?family=Oswald:wght@500;700&family=Arimo:wght@400;700&display=swap">
<style>
  :root {
    --gold-dark: #6e521d;
    --gold-mid: #a98a4c;
    --gold-light: #d8bf86;
    --text-gold: #7a5a1d;
    --ink: #0c0c0c;
    --silver-light: #f7f7f7;
    --silver-mid: #d9d9d9;
    --silver-dark: #b9b9b9;
    --white: #ffffff;
    --leather: #1d1d1d;
    --wood: #8a4a22;
    --pine: #2f5a2a;
  }
  * { margin: 0; padding: 0; box-sizing: border-box; }
  html, body { width: 1200px; height: 660px; overflow: hidden; }
  body { font-family: "Arimo", Arial, sans-serif; }

  .banner {
    position: relative;
    width: 1200px;
    height: 660px;
    overflow: hidden;
    background:
      radial-gradient(circle at 20% 60%, rgba(255,255,255,.9) 0 40px, transparent 90px),
      radial-gradient(circle at 70% 75%, rgba(255,255,255,.8) 0 50px, transparent 110px),
      radial-gradient(circle at 95% 30%, rgba(255,255,255,.7) 0 40px, transparent 90px),
      radial-gradient(ellipse at 50% 50%, var(--silver-light) 0%, var(--silver-mid) 70%, var(--silver-dark) 100%);
  }

  .header-band {
    position: absolute;
    left: 0; top: 0;
    width: 1200px; height: 110px;
    background: linear-gradient(90deg, var(--gold-dark) 0%, var(--gold-mid) 30%, var(--gold-light) 50%, var(--gold-mid) 70%, var(--gold-dark) 100%);
    box-shadow: 0 4px 10px rgba(0,0,0,.25);
  }
  .header-pointer {
    position: absolute;
    left: 552px; top: 108px;
  }
  .header-title {
    position: absolute;
    left: 0; top: 8px; width: 1200px;
    text-align: center;
    font-family: "Oswald", "Arial Narrow", sans-serif;
    font-weight: 700;
    font-size: 70px;
    letter-spacing: 2px;
    line-height: 90px;
    color: #eeeeee;
    background: linear-gradient(180deg, #ffffff 0%, #e6e6e6 50%, #a9a9a9 100%);
    -webkit-background-clip: text;
    background-clip: text;
    -webkit-text-fill-color: transparent;
    filter: drop-shadow(0 3px 3px rgba(0,0,0,.45));
  }
  .header-stars { position: absolute; top: 46px; }
  .header-stars.left { left: 18px; }
  .header-stars.right { left: 905px; }

  .chair-photo {
    position: absolute;
    left: 44px; top: 232px;
    width: 345px; height: 372px;
    border-radius: 40% 30% 10% 10%;
    background: radial-gradient(ellipse at 55% 55%, var(--wood) 0%, var(--leather) 55%, rgba(30,30,30,0) 75%);
  }
  .ottoman-photo {
    position: absolute;
    left: 445px; top: 388px;
    width: 205px; height: 200px;
    border-radius: 30% 30% 10% 10%;
    background: radial-gradient(ellipse at 50% 40%, var(--wood) 0%, var(--leather) 50%, rgba(30,30,30,0) 75%);
  }

  .price-seal { position: absolute; left: 298px; top: 168px; }
  .seal-text { font-family: "Oswald", sans-serif; font-weight: 500; }

  .offer-text {
    position: absolute;
    left: 690px; top: 248px;
    width: 440px;
    text-align: center;
    font-weight: 700;
    line-height: 62px;
  }
  .offer-text .highlight { color: var(--text-gold); font-size: 52px; }
  .offer-text .line { color: var(--ink); font-weight: 400; font-size: 55px; }

  .garland {
    position: absolute;
    left: 752px; top: 436px;
    width: 322px; height: 150px;
    border-radius: 50%;
    background: radial-gradient(ellipse at 50% 55%, var(--pine) 0%, rgba(47,90,42,.6) 45%, rgba(47,90,42,0) 72%);
  }
  .shop-button {
    position: absolute;
    left: 794px; top: 470px;
    width: 232px; height: 76px;
    display: flex; align-items: center; justify-content: center;
    border-radius: 8px;
    border: 3px solid var(--gold-light);
    background: linear-gradient(180deg, var(--gold-mid) 0%, var(--gold-dark) 100%);
    box-shadow: 0 4px 8px rgba(0,0,0,.4);
    font-family: "Oswald", sans-serif;
    font-weight: 700;
    font-size: 44px;
    color: #f1f1f1;
    text-decoration: none;
    text-shadow: 0 2px 3px rgba(0,0,0,.6);
  }

  .delivery-bar {
    position: absolute;
    left: 0; top: 608px;
    width: 439px; height: 34px;
    background: var(--gold-dark);
    display: flex; align-items: center;
    padding-left: 40px; gap: 8px;
    color: var(--white);
    font-weight: 700;
    font-size: 16px;
    letter-spacing: .3px;
  }
</style>
</head>
<body>
<main class="banner">
  <header>
    <div class="header-band"></div>
    <svg class="header-pointer" width="96" height="52" viewBox="0 0 96 52" aria-hidden="true">
      <defs><linearGradient id="pointerFill" x1="0" y1="0" x2="0" y2="1"><stop offset="0" stop-color="#d8bf86"/><stop offset="1" stop-color="#a98a4c"/></linearGradient></defs>
      <polygon points="0,0 96,0 48,52" fill="url(#pointerFill)"/>
    </svg>
    <svg class="header-stars left" width="280" height="16" viewBox="0 0 280 16" aria-hidden="true">
      <g fill="#ffffff">
        <polygon points="8,0 10,5 16,5 11,8 13,14 8,10 3,14 5,8 0,5 6,5" transform="translate(0,0)"/>
        <polygon points="8,0 10,5 16,5 11,8 13,14 8,10 3,14 5,8 0,5 6,5" transform="translate(63,0)"/>
        <polygon points="8,0 10,5 16,5 11,8 13,14 8,10 3,14 5,8 0,5 6,5" transform="translate(126,0)"/>
        <polygon points="8,0 10,5 16,5 11,8 13,14 8,10 3,14 5,8 0,5 6,5" transform="translate(189,0)"/>
        <polygon points="8,0 10,5 16,5 11,8 13,14 8,10 3,14 5,8 0,5 6,5" transform="translate(252,0)"/>
      </g>
    </svg>
    <svg class="header-stars right" width="280" height="16" viewBox="0 0 280 16" aria-hidden="true">
      <g fill="#ffffff">
        <polygon points="8,0 10,5 16,5 11,8 13,14 8,10 3,14 5,8 0,5 6,5" transform="translate(0,0)"/>
        <polygon points="8,0 10,5 16,5 11,8 13,14 8,10 3,14 5,8 0,5 6,5" transform="translate(63,0)"/>
        <polygon points="8,0 10,5 16,5 11,8 13,14 8,10 3,14 5,8 0,5 6,5" transform="translate(126,0)"/>
        <polygon points="8,0 10,5 16,5 11,8 13,14 8,10 3,14 5,8 0,5 6,5" transform="translate(189,0)"/>
        <polygon points="8,0 10,5 16,5 11,8 13,14 8,10 3,14 5,8 0,5 6,5" transform="translate(252,0)"/>
      </g>
    </svg>
    <h1 class="header-title">CHRISTMAS SPECIAL</h1>
  </header>

  <div class="chair-photo" role="img" aria-label="Vortan Tidal Seat in black leather with rosewood shells, side view"></div>
  <div class="ottoman-photo" role="img" aria-label="Matching Tidal Seat ottoman in black leather and rosewood"></div>

  <svg class="price-seal" width="212" height="212" viewBox="0 0 212 212" role="img" aria-label="Super Christmas Special: was 1998 €, now 799 €">
    <circle cx="106" cy="106" r="98" fill="#f4efe4" stroke="#7a5a1d" stroke-width="10" stroke-dasharray="5 3"/>
    <circle cx="106" cy="106" r="93" fill="#f4efe4"/>
    <circle cx="106" cy="106" r="90" fill="none" stroke="#7a5a1d" stroke-width="1.5"/>
    <circle cx="106" cy="106" r="66" fill="#7a5a1d"/>
    <defs><path id="sealRing" d="M106,106 m-78,0 a78,78 0 1,1 156,0 a78,78 0 1,1 -156,0"/></defs>
    <text class="seal-text" font-size="15" fill="#7a5a1d" letter-spacing="1.5">
      <textPath href="#sealRing">SUPER CHRISTMAS SPECIAL – SUPER CHRISTMAS SPECIAL –</textPath>
    </text>
    <g transform="rotate(-15 106 106)" text-anchor="middle" fill="#ffffff" font-family="Oswald, sans-serif">
      <text x="106" y="76" font-size="14">was</text>
      <text x="106" y="96" font-size="20">1998 €</text>
      <line x1="74" y1="90" x2="140" y2="90" stroke="#ffffff" stroke-width="2"/>
      <text x="106" y="114" font-size="14">NOW!</text>
      <text x="106" y="150" font-size="40" font-weight="700">799€</text>
    </g>
  </svg>

  <section class="offer-text">
    <p class="highlight">ONLY 24 PIECES</p>
    <p class="line">&amp; ONLY WHILE</p>
    <p class="line">STOCK LASTS!</p>
  </section>

  <div class="garland" role="img" aria-label="Pine garland with red and gold baubles and a bow"></div>
  <a class="shop-button" href="#">SHOP NOW !</a>

  <footer class="delivery-bar">
    <span>FREE DELIVERY ON ALL ORDERS !</span>
    <svg width="32" height="18" viewBox="0 0 32 18" aria-hidden="true">
      <g fill="#ffffff">
        <rect x="0" y="1" width="19" height="12" rx="1"/>
        <path d="M20 4h6l5 5v4h-11z"/>
        <circle cx="6" cy="15" r="2.6"/>
        <circle cx="25" cy="15" r="2.6"/>
      </g>
    </svg>
  </footer>
</main>
</body>
</html>
```